Packiging of mouse trap

We need a packiging for a new mousetrap called 'Quillnest'. It is a mouse/rat trap. We want to have it pretty simple and modern. The logo of the mouse trap is in the attachment and the measures of the packaging also (don't look at the design, it has nothing to do with us). It's needs to stand out in between the other packaging due to it's simplicity and modern touch.

Font styles to use
Sans Serif

Requirements
Must have
• Simplicity, modern
Should not have
• Too many colors

```html
<!DOCTYPE html>
<html lang="en">
<head>
<meta charset="utf-8">
<title>Quillnest Mouse Trap – Box Dieline</title>
<link href="https://fonts.googleapis.com/css2?family=Montserrat:wght@400;500;600;700;800&display=swap" rel="stylesheet">
<style>
  :root {
    --paper: #ffffff;
    --ink: #000000;
    --type: #ffffff;
    --fold: #2b3b3d;
    --label: #1a1a1a;
    --fur-dark: #0b0b0b;
    --fur-mid: #2a2a2a;
  }
  * { box-sizing: border-box; margin: 0; padding: 0; }
  html, body { width: 1200px; height: 1000px; overflow: hidden; background: var(--paper); }
  body { font-family: "Montserrat", sans-serif; color: var(--type); }
  .canvas { position: relative; width: 1200px; height: 1000px; }

  .size-label {
    position: absolute; left: 329px; top: 36px; width: 430px; text-align: center;
    color: var(--label); font-size: 22px; font-weight: 400; letter-spacing: 0.3px;
  }

  .panel, .flap {
    position: absolute; background: var(--ink);
    outline: 1px solid var(--fold); overflow: hidden;
  }
  .flap { border-radius: 3px; }
  .ear { position: absolute; }
  .ear path { fill: var(--ink); stroke: var(--fold); stroke-width: 1; }

  .wordmark {
    position: absolute; font-weight: 800; color: var(--type);
    letter-spacing: -0.5px; white-space: nowrap; line-height: 1;
    transform: translate(-50%, -50%);
  }
  .wordmark.upright-180 { transform: translate(-50%, -50%) rotate(180deg); }
  .wordmark.vertical { transform: translate(-50%, -50%) rotate(-90deg); }

  .spaced-word {
    position: absolute; font-weight: 500; letter-spacing: 4px; white-space: nowrap;
    transform: translate(-50%, -50%); line-height: 1;
  }
  .spaced-word.vertical { transform: translate(-50%, -50%) rotate(-90deg); letter-spacing: 2px; }

  .fur-photo {
    position: absolute;
    background: radial-gradient(ellipse at 40% 55%, var(--fur-mid) 0%, #181818 45%, var(--fur-dark) 80%);
  }
  .fur-photo.band {
    background: linear-gradient(180deg, #151515 0%, #262626 50%, #121212 100%);
  }
  .guide-line { position: absolute; width: 1px; background: #6a6a6a; }

  .copy {
    position: absolute; font-size: 6.6px; line-height: 1.5; text-align: justify; font-weight: 400;
  }
  .copy p + p { margin-top: 2px; }
  .copy-heading {
    position: absolute; font-size: 8px; font-weight: 700; text-align: center; letter-spacing: 0.3px;
  }
  .steps { position: absolute; font-size: 6.6px; line-height: 1.5; text-align: justify; padding-left: 10px; }
  .steps li { margin-bottom: 4px; }
  .maker {
    position: absolute; font-size: 6.8px; line-height: 1.35; text-align: center; font-weight: 500;
  }
  .maker strong { font-weight: 700; }
  .slot { position: absolute; background: var(--paper); }
</style>
</head>
<body>
<div class="canvas">

  <div class="size-label">92*113*260mm</div>

  <!-- left tuck ears -->
  <svg class="ear ear-top" style="left:150px; top:125px;" width="215" height="166" viewBox="0 0 215 166">
    <path d="M0.5,165.5 L0.5,120 C0.5,45 55,0.5 130,0.5 L158,0.5 C176,0.5 182,22 174,38 C168,52 188,62 214.5,64 L214.5,165.5 Z"/>
  </svg>
  <svg class="ear ear-bottom" style="left:150px; top:795px;" width="215" height="142" viewBox="0 0 215 142">
    <path d="M0.5,0.5 L0.5,40 C0.5,100 50,141.5 125,141.5 L160,141.5 C176,141.5 182,124 176,110 C170,96 188,88 214.5,86 L214.5,0.5 Z"/>
  </svg>

  <!-- top flaps -->
  <div class="flap flap-top-front" style="left:329px; top:90px; width:212px; height:200px;"></div>
  <div class="flap flap-top-lid" style="left:544px; top:90px; width:215px; height:200px;">
    <div class="wordmark" style="left:107px; top:110px; font-size:31px;">Quillnest</div>
  </div>
  <div class="flap flap-top-back" style="left:763px; top:90px; width:168px; height:200px;">
    <div class="slot" style="left:0; top:81px; width:8px; height:50px;"></div>
  </div>

  <!-- side panel with vertical branding -->
  <div class="panel panel-side" style="left:150px; top:290px; width:215px; height:506px;">
    <div class="spaced-word vertical" style="left:106px; top:50px; font-size:13px;">TRAP</div>
    <div class="fur-photo band" role="img" aria-label="Close-up photo of a dark mouse's fur" style="left:31px; top:144px; width:156px; height:62px;"></div>
    <div class="spaced-word vertical" style="left:106px; top:265px; font-size:13px;">MOUSE</div>
    <div class="wordmark vertical" style="left:106px; top:400px; font-size:30px;">Quillnest</div>
  </div>

  <!-- front panel -->
  <div class="panel panel-front" style="left:365px; top:290px; width:179px; height:506px;">
    <div class="wordmark" style="left:90px; top:88px; font-size:27px;">Quillnest</div>
    <div class="spaced-word" style="left:90px; top:214px; font-size:17px;">MOUSE</div>
    <div class="fur-photo" role="img" aria-label="Dark close-up photo of a mouse in shadow" style="left:4px; top:237px; width:156px; height:180px;"></div>
    <div class="guide-line" style="left:50px; top:232px; height:195px;"></div>
    <div class="guide-line" style="left:95px; top:232px; height:195px;"></div>
    <div class="spaced-word" style="left:90px; top:432px; font-size:17px;">TRAP</div>
  </div>

  <!-- description panel -->
  <div class="panel panel-info" style="left:544px; top:290px; width:215px; height:506px;">
    <div class="wordmark" style="left:107px; top:52px; font-size:18px;">Quillnest</div>
    <div class="copy" style="left:26px; top:86px; width:165px;">
      <p>Quillnest is a clean, reusable trap for mice and small rats. It sets in seconds, closes quickly and keeps the catch out of sight. The sealed body is easy to wipe and safe to handle. Place it along walls where droppings appear, and check it every morning.</p>
      <p>Made from sturdy recycled plastic with a steel spring. No poison and no glue, so it suits kitchens, garages and sheds. One trap covers a small room.</p>
    </div>
    <div class="copy-heading" style="left:26px; top:362px; width:165px;">WARNING</div>
    <div class="copy" style="left:26px; top:376px; width:165px;">
      <p>Keep away from children and pets. Handle the spring with care and wear gloves when emptying. Do not set the trap near food. Wash hands after use. Dispose of the catch in a sealed bag.</p>
    </div>
  </div>

  <!-- instructions panel -->
  <div class="panel panel-instructions" style="left:759px; top:290px; width:178px; height:506px;">
    <div class="copy-heading" style="left:20px; top:44px; width:140px;">HOW TO USE</div>
    <ol class="steps" style="left:18px; top:58px; width:142px;">
      <li>Open the lid and add a small piece of bait to the cup.</li>
      <li>Press the lever down until it clicks into the set position.</li>
      <li>Place the trap against a wall with the entrance facing the path mice use most often.</li>
      <li>Check the trap daily and reset it after each catch.</li>
      <li>Rinse with warm water and let it dry before storing.</li>
    </ol>
    <div class="maker" style="left:10px; top:354px; width:158px;">
      <strong>QUILLNEST</strong><br>
      Mouse Trap<br>
      Sample Series Number<br>
      Sample Address, Unit #<br>
      City, 12345<br>
      <strong>www.quillnest-traps.com</strong>
    </div>
  </div>

  <!-- glue flap -->
  <div class="panel panel-glue" style="left:940px; top:137px; width:110px; height:818px;"></div>

  <!-- bottom flaps -->
  <div class="flap flap-bottom-front" style="left:329px; top:796px; width:212px; height:169px;"></div>
  <div class="flap flap-bottom-lid" style="left:544px; top:796px; width:215px; height:169px;">
    <div class="wordmark upright-180" style="left:107px; top:70px; font-size:31px;">Quillnest</div>
  </div>
  <div class="flap flap-bottom-back" style="left:763px; top:796px; width:168px; height:169px;"></div>

</div>
</body>
</html>
```